Business Card Design for Tax Accounting Company

I need design files that can be edited to add new professional designations onto the end of my name once complete. I need design files that can be edited for new employees. I also need the design files to be able to upload into PrintHollow for new orders. I've attached multiple logo files with varying file extensions to help with the design.
Please include the following contact information:
Marcus Tenley, CPA, CMA, CFE, CGMA
Founder & CEO
C (480) 517.3082
F (555) 391.7258
418 W Larkspur Ave
Larkmoor, AZ 85390
Updates
I need the business card to include the following contact info:
C: (555)517.3082
F: (555) 391.7258
mt@QuarrystoneLedgerworks.com
www.MarcusRTenley.com
Address to be included is
418 W Larkspur Ave
Larkmoor, AZ 85390
Business Cards are double sided
Target Market(s)
Business owners $1M+ annual revenue, especially for the construction and technology industries
Industry/Entity Type
Accounting & Tax
Contact Information for Business Card
Contact information and logo
Look and feel

```html
<!DOCTYPE html>
<html lang="en">
<head>
<meta charset="utf-8">
<title>Quarrystone Ledgerworks – Business Card</title>
<link rel="stylesheet" href="https://fonts.googleapis.com/css2?family=Noto+Serif:wght@400;700;900&display=swap">
<style>
  :root {
    --navy: #1f2d63;
    --orange: #c9561f;
    --ink: #3a3a3a;
    --white: #ffffff;
    --backdrop: #e6e6e8;
  }
  * { box-sizing: border-box; margin: 0; padding: 0; }
  html, body { width: 1200px; height: 963px; overflow: hidden; }
  body {
    background: var(--backdrop);
    font-family: "Noto Serif", Georgia, serif;
    display: flex;
    flex-direction: column;
    align-items: center;
    justify-content: center;
    gap: 48px;
  }
  .card {
    width: 700px;
    height: 400px;
    border-radius: 18px;
    box-shadow: 0 10px 30px rgba(0,0,0,.18);
    position: relative;
    overflow: hidden;
  }
  /* Front */
  .card-front {
    background: var(--white);
    display: flex;
    align-items: center;
    padding: 0 36px;
  }
  .brand {
    width: 250px;
    flex: none;
    display: flex;
    flex-direction: column;
    align-items: flex-start;
  }
  .brand-mark {
    display: flex;
    align-items: center;
    gap: 12px;
  }
  .brand-dot {
    width: 22px; height: 22px;
    border-radius: 50%;
    background: var(--orange);
    flex: none;
  }
  .brand-name {
    color: var(--navy);
    font-weight: 900;
    font-size: 27px;
    line-height: 1.08;
  }
  .tagline {
    margin-top: 10px;
    color: var(--navy);
    font-size: 10.5px;
    white-space: nowrap;
  }
  .divider {
    width: 1.5px;
    height: 190px;
    background: var(--orange);
    margin: 0 26px;
    flex: none;
  }
  .details { flex: 1; min-width: 0; }
  .person-name {
    color: var(--navy);
    font-weight: 900;
    font-size: 24px;
    letter-spacing: .5px;
    text-transform: uppercase;
    line-height: 1.15;
  }
  .credentials {
    color: var(--orange);
    font-size: 16px;
    margin-bottom: 12px;
  }
  .contact-list { list-style: none; }
  .contact-list li {
    display: flex;
    align-items: center;
    gap: 8px;
    color: var(--ink);
    font-size: 13.5px;
    line-height: 1.7;
    white-space: nowrap;
  }
  .contact-list svg { width: 12px; height: 12px; fill: var(--navy); flex: none; }
  /* Back */
  .card-back {
    background: var(--navy);
    display: flex;
    flex-direction: column;
    align-items: center;
    justify-content: center;
    gap: 20px;
  }
  .card-back .brand-name { color: var(--white); font-size: 40px; white-space: nowrap; }
  .card-back .brand-dot { width: 30px; height: 30px; }
  .card-back .tagline { color: var(--white); font-size: 16px; margin: 0; }
</style>
</head>
<body>
  <section class="card card-front" aria-label="Card front">
    <div class="brand">
      <div class="brand-mark">
        <span class="brand-dot"></span>
        <span class="brand-name">Quarrystone<br>Ledgerworks</span>
      </div>
      <p class="tagline">Clear Numbers. Steady Guidance. Lasting Growth.</p>
    </div>
    <div class="divider"></div>
    <div class="details">
      <h1 class="person-name">Marcus Tenley</h1>
      <p class="credentials">CPA, CMA, CFE, CGMA</p>
      <ul class="contact-list">
        <li><svg viewBox="0 0 24 24"><path d="M6.6 10.8a15 15 0 0 0 6.6 6.6l2.2-2.2c.3-.3.7-.4 1-.2 1.1.4 2.3.6 3.6.6.6 0 1 .4 1 1V20c0 .6-.4 1-1 1C10.6 21 3 13.4 3 4c0-.6.4-1 1-1h3.5c.6 0 1 .4 1 1 0 1.3.2 2.5.6 3.6.1.3 0 .7-.2 1z"/></svg>(555)517.3082</li>
        <li><svg viewBox="0 0 24 24"><path d="M6 2h12v6H6zM4 9h16a2 2 0 0 1 2 2v7h-4v4H6v-4H2v-7a2 2 0 0 1 2-2zm4 7v4h8v-4z"/></svg>(555) 391.7258</li>
        <li><svg viewBox="0 0 24 24"><path d="M2 5h20v14H2zm2 2v.5l8 5 8-5V7l-8 5z"/></svg>mt@QuarrystoneLedgerworks.com</li>
        <li><svg viewBox="0 0 24 24"><path d="M12 2a10 10 0 1 0 0 20 10 10 0 0 0 0-20zm0 2c.9 1.2 1.6 2.6 2 4h-4c.4-1.4 1.1-2.8 2-4zM4.3 14a8 8 0 0 1 0-4h3.4a16 16 0 0 0 0 4zm.9 2h2.9c.4 1.3.9 2.5 1.6 3.6A8 8 0 0 1 5.2 16zm2.9-8H5.2a8 8 0 0 1 4.5-3.6C9 5.5 8.5 6.7 8.1 8zM12 20c-.9-1.2-1.6-2.6-2-4h4c-.4 1.4-1.1 2.8-2 4zm2.3-6H9.7a14 14 0 0 1 0-4h4.6a14 14 0 0 1 0 4z"/></svg>www.MarcusRTenley.com</li>
        <li><svg viewBox="0 0 24 24"><path d="M12 2a7 7 0 0 0-7 7c0 5 7 13 7 13s7-8 7-13a7 7 0 0 0-7-7zm0 9.5a2.5 2.5 0 1 1 0-5 2.5 2.5 0 0 1 0 5z"/></svg>418 W Larkspur Ave, Larkmoor, AZ 85390</li>
      </ul>
    </div>
  </section>

  <section class="card card-back" aria-label="Card back">
    <div class="brand-mark">
      <span class="brand-dot"></span>
      <span class="brand-name">Quarrystone Ledgerworks</span>
    </div>
    <p class="tagline">Clear Numbers. Steady Guidance. Lasting Growth.</p>
  </section>
</body>
</html>
```